Psychology and personal development service needs an awesome Web Design

Hi, we are Bright Path Studio, a psychology and personal development service located in Melbourne Australia. We already have a website www.brightpathstudio.org but it is in great need of a makeover! We add to the website regularly with articles and so we need a space to archive these when they come off the main page, and we have products that we would like to sell internationally so we need a shop page that can convert currencies for international sales and calculate postage and handling. We have a Chatterly page that we would like to link as well as a newsletter that we would like to archive on the website. We have just had a logo designed through mark forge and would like to incorporate this into our website. We want something with high visual impact and uncluttered.
We also run workshops and events so need a tab for this.
Thanks for getting on board!

```html
<!DOCTYPE html>
<html lang="en">
<head>
<meta charset="utf-8">
<title>Bright Path Studio</title>
<link href="https://fonts.googleapis.com/css2?family=Open+Sans:wght@400;600;700&display=swap" rel="stylesheet">
<style>
:root{
  --teal:#36b49f;
  --purple:#6b3f8e;
  --text:#666;
  --light:#999;
  --line:#e6e6e6;
  --footer:#2c2c2c;
  --footer-deep:#232323;
  --footer-text:#a9a9a9;
  --white:#fff;
}
*{margin:0;padding:0;box-sizing:border-box}
html,body{width:1200px;height:2542px;overflow:hidden}
body{font-family:"Open Sans",Arial,sans-serif;color:var(--text);background:var(--white);position:relative}
.abs{position:absolute}
.hero{left:0;top:0;width:1200px;height:702px;background:linear-gradient(100deg,#c9d3cf 0%,#e6e2d6 30%,#d7c1a6 55%,#8a5a3b 75%,#c9b8a6 100%)}
.brand-panel{left:139px;top:37px;width:212px;background:var(--white);box-shadow:0 2px 6px rgba(0,0,0,.2)}
.brand{height:138px;display:flex;align-items:center;justify-content:center;gap:10px;padding:0 12px}
.brand-dot{width:34px;height:34px;border-radius:50%;background:var(--purple);flex:none}
.brand-name{color:var(--purple);font-weight:600;font-size:22px;line-height:1.05}
.menu{list-style:none}
.menu li{height:28.4px;line-height:28.4px;padding-left:41px;font-size:9.5px;color:#777;border-top:1px solid #eee;letter-spacing:.3px}
.menu li.active{background:var(--teal);color:var(--white);border-top:none}
.band{left:0;top:702px;width:1200px;height:58px;background:var(--teal);color:var(--white);display:flex;align-items:center;justify-content:center;font-size:19px;font-weight:600;letter-spacing:.3px}
.band svg{position:absolute;top:19px}
.sec-head{font-size:17px;font-weight:600;color:var(--purple);display:flex;align-items:center;gap:10px;text-transform:uppercase}
.sec-head .hi{color:var(--teal)}
.sec-head::after{content:"";flex:1;height:3px;background:#f0f0f0}
.divider{left:790px;top:835px;width:1px;height:700px;background:var(--line)}
.article{left:139px;width:609px;height:220px}
.article .thumb{position:absolute;left:0;top:0;width:286px;height:220px}
.article .body{position:absolute;left:314px;top:6px;width:295px}
.article h3{color:var(--purple);font-size:18px;font-weight:600;margin-bottom:16px}
.meta{font-size:10.5px;color:#b5b5b5;display:flex;align-items:center;gap:7px;margin-bottom:10px}
.meta i{display:inline-block;width:11px;height:9px;background:#c9c9c9;border-radius:2px}
.excerpt{font-size:11px;line-height:20px;color:#777;margin-top:14px}
.btn{display:inline-block;margin-top:22px;background:var(--teal);color:var(--white);font-size:10px;font-weight:700;padding:9px 19px;border-radius:2px}
.event{left:830px;width:231px;text-align:center}
.event .thumb{width:231px;height:136px}
.event h4{font-size:12.5px;font-weight:600;color:#555;margin:14px 0 9px}
.event p{font-size:10.5px;line-height:16px;color:#888}
.product{top:1659px;width:166px;height:233px;border:1px solid #e2e2e2;box-shadow:0 1px 3px rgba(0,0,0,.08);text-align:center}
.product .thumb{width:80px;height:108px;margin:18px auto 0}
.product h4{color:var(--purple);font-size:13.5px;font-weight:600;margin:12px 0 6px}
.product p{font-size:10.5px;line-height:16px;color:#888;padding:0 14px}
.product .more{display:block;margin-top:8px;font-size:9px;font-weight:700;color:var(--teal)}
.social-box{left:139px;top:1934px;width:922px;height:212px;border:1px solid #e2e2e2;background:#fafafa}
.sb-head{position:absolute;left:18px;top:18px;display:flex;gap:10px;align-items:center}
.sb-dot{width:36px;height:36px;border-radius:50%;background:var(--purple)}
.sb-name{font-size:11px;color:#3b5177;font-weight:600}
.sb-like{display:inline-block;margin-top:3px;background:#5a6fa0;color:#fff;font-size:9px;padding:1px 5px}
.sb-count{position:absolute;left:18px;top:66px;font-size:10px;color:#555}
.sb-faces{position:absolute;left:17px;top:88px;width:890px;height:85px;background:linear-gradient(90deg,#b48a6e,#d9c6b5,#8c6b58,#c7a58b,#9f8677,#d3b69b)}
.sb-foot{position:absolute;left:18px;top:185px;font-size:8.5px;color:#666;display:flex;align-items:center;gap:5px}
.sb-foot i{width:9px;height:9px;background:#5a6fa0;display:inline-block}
.footer{left:0;top:2180px;width:1200px;height:295px;background:var(--footer)}
.f-head{font-size:13.5px;font-weight:600;color:var(--white);text-transform:uppercase}
.f-head .hi{color:var(--teal)}
.f-col{top:2214px}
.contact-row{display:flex;gap:16px;align-items:flex-start;font-size:10.5px;line-height:17px;color:var(--footer-text);padding:18px 0;border-bottom:1px solid #3a3a3a}
.contact-row:last-child{border-bottom:none}
.ic{width:28px;height:28px;border-radius:50%;background:#3c3c3c;flex:none;display:flex;align-items:center;justify-content:center}
.works{display:grid;grid-template-columns:93px 93px;gap:8px;margin-top:44px}
.works div{height:74px}
.dolist{list-style:none;margin-top:40px}
.dolist li{font-size:10.5px;color:var(--footer-text);line-height:29.5px}
.dolist li::before{content:"";display:inline-block;width:4px;height:4px;border-radius:50%;background:var(--teal);margin-right:8px;vertical-align:middle}
.ev-thumb{width:178px;height:118px;margin-top:44px}
.ev-title{font-size:11px;color:var(--teal);font-weight:600;margin-top:12px}
.ev-meta{font-size:10.5px;color:var(--footer-text);margin-top:2px}
.bottom{left:0;top:2475px;width:1200px;height:67px;background:var(--footer-deep)}
.copy{position:absolute;left:139px;top:26px;font-size:10px;color:var(--footer-text)}
.sq{position:absolute;top:20px;width:26px;height:26px;background:#555;border-radius:3px}
</style>
</head>
<body>

<div class="abs hero" role="img" aria-label="Photo of a stressed woman holding her temples in front of a snowy winter tree"></div>

<nav class="abs brand-panel">
  <div class="brand"><span class="brand-dot"></span><span class="brand-name">Bright Path Studio</span></div>
  <ul class="menu">
    <li class="active">HOME PAGE</li><li>ABOUT US</li><li>BOOKS</li><li>ONLINE STORE</li><li>CONTACT US</li>
    <li>BODY TALK</li><li>RELATIONSHIPS</li><li>PARENTS &amp; CHILDREN</li><li>TECHNOLOGY</li><li>SUCCESS</li>
    <li>TRANSFORMING</li><li>DISCOVER SELF WORTH</li><li>I DON'T HAVE TIME</li><li>PARASITES</li><li>SURFING</li>
    <li>CREATING A LEGACY</li><li>MISCELLANEOUS</li>
  </ul>
</nav>

<div class="abs band">
  <svg style="left:138px" width="14" height="20" viewBox="0 0 14 20"><path d="M11 2 3 10l8 8" fill="none" stroke="#fff" stroke-width="3"/></svg>
  WE ARE A PSYCHOLOGY &amp; PERSONAL DEVELOPMENT CENTER
  <svg style="left:1045px" width="14" height="20" viewBox="0 0 14 20"><path d="M3 2l8 8-8 8" fill="none" stroke="#fff" stroke-width="3"/></svg>
</div>

<h2 class="abs sec-head" style="left:139px;top:790px;width:609px"><span><span class="hi">Latest</span> Articles</span></h2>
<h2 class="abs sec-head" style="left:830px;top:790px;width:231px"><span><span class="hi">Workshop</span> / Events</span></h2>
<div class="abs divider"></div>

<article class="abs article" style="top:839px">
  <div class="thumb" role="img" aria-label="Illustration of a head silhouette filled with gears" style="background:linear-gradient(135deg,#4a5564,#1e2530)"></div>
  <div class="body">
    <h3>Cum sociis natoqued</h3>
    <div class="meta"><i></i>Psychology , Sunday Morning &nbsp;/&nbsp; <i></i>Mara Quill</div>
    <div class="meta"><i></i>Fit Row, Life Book, Sunday Morning &nbsp;/&nbsp; <i></i>0</div>
    <p class="excerpt">Lorem ipsum dolor sit amet, consectetur adipisici elit, sed eiusmod tempor incidunt ut labore et dolore magna aliqua. Idque Caesaris facere voluntate liceret.</p>
    <span class="btn">READ MORE</span>
  </div>
</article>
<article class="abs article" style="top:1092px">
  <div class="thumb" role="img" aria-label="Photo of a counsellor taking notes with a thoughtful young woman" style="background:linear-gradient(135deg,#d8d2c4,#b9b6ad)"></div>
  <div class="body">
    <h3>Cum sociis natoque</h3>
    <div class="meta"><i></i>Psychology , Sunday Morning &nbsp;/&nbsp; <i></i>Mara Quill</div>
    <div class="meta"><i></i>Fit Row, Life Book, Sunday Morning &nbsp;/&nbsp; <i></i>0</div>
    <p class="excerpt">Lorem ipsum dolor sit amet, consectetur adipisici elit, sed eiusmod tempor incidunt ut labore et dolore magna aliqua. Idque Caesaris facere voluntate liceret.</p>
    <span class="btn">READ MORE</span>
  </div>
</article>
<article class="abs article" style="top:1349px">
  <div class="thumb" role="img" aria-label="Photo of a worried woman in a therapy session" style="background:linear-gradient(135deg,#e3e3e0,#b8b3ad)"></div>
  <div class="body">
    <h3>Cum sociis natoque</h3>
    <div class="meta"><i></i>Psychology , Sunday Morning &nbsp;/&nbsp; <i></i>Mara Quill</div>
    <div class="meta"><i></i>Fit Row, Life Book, Sunday Morning &nbsp;/&nbsp; <i></i>0</div>
    <p class="excerpt">Lorem ipsum dolor sit amet, consectetur adipisici elit, sed eiusmod tempor incidunt ut labore et dolore magna aliqua. Idque Caesaris facere voluntate liceret.</p>
    <span class="btn">READ MORE</span>
  </div>
</article>

<div class="abs event" style="top:839px">
  <div class="thumb" role="img" aria-label="Photo of a group workshop session" style="background:linear-gradient(135deg,#cfcac4,#8d7f74)"></div>
  <h4>Sem Porta Mollis Parturient</h4>
  <p>Lorem ipsum dolor sit amet, consectetur adipisici elit, sed eiusmod tempor incidunt ut labore et dolore magna aliqua. Idque Caesaris</p>
</div>
<div class="abs event" style="top:1097px">
  <div class="thumb" role="img" aria-label="Photo of a woman with a headache" style="background:linear-gradient(135deg,#e8e6df,#7a5a48)"></div>
  <h4>Sem Porta Mollis Parturient</h4>
  <p>Lorem ipsum dolor sit amet, consectetur adipisici elit, sed eiusmod tempor incidunt ut labore et dolore magna aliqua. Idque Caesaris</p>
</div>
<div class="abs event" style="top:1359px">
  <div class="thumb" role="img" aria-label="Vintage phrenology head chart" style="background:linear-gradient(135deg,#e6b84a,#c8922a)"></div>
  <h4>Sem Porta Mollis Parturient</h4>
  <p>Lorem ipsum dolor sit amet, consectetur adipisici elit, sed eiusmod tempor incidunt</p>
</div>

<h2 class="abs sec-head" style="left:139px;top:1608px;width:922px"><span><span class="hi">Our</span> Products</span></h2>

<div class="abs product" style="left:139px">
  <div class="thumb" role="img" aria-label="Book cover" style="background:linear-gradient(#5a2e22,#2e1a14);width:66px"></div>
  <h4>Simplicity Leads</h4><p>Lorem ipsum dolor sit amet, consectetur adipisici elit,</p><span class="more">READ MORE</span>
</div>
<div class="abs product" style="left:329px">
  <div class="thumb" role="img" aria-label="Book cover" style="background:linear-gradient(90deg,#bdbdbd,#f0f0f0);width:70px"></div>
  <h4>Positive Emotion</h4><p>Lorem ipsum dolor sit amet, consectetur adipisici elit,</p><span class="more">READ MORE</span>
</div>
<div class="abs product" style="left:519px">
  <div class="thumb" role="img" aria-label="DVD box set" style="background:linear-gradient(135deg,#d9d9d9,#3d4f7a);width:100px;height:70px;margin-top:45px"></div>
  <h4>Hold The Vision</h4><p>Lorem ipsum dolor sit amet, consectetur adipisici elit,</p><span class="more">READ MORE</span>
</div>
<div class="abs product" style="left:708px">
  <div class="thumb" role="img" aria-label="Audio disc set" style="background:linear-gradient(135deg,#2f4f8c,#9bb3d8);width:112px;height:76px;margin-top:40px"></div>
  <h4>Thinking</h4><p>Lorem ipsum dolor sit amet, consectetur adipisici elit,</p><span class="more">READ MORE</span>
</div>
<div class="abs product" style="left:895px">
  <div class="thumb" role="img" aria-label="DVD case with discs" style="background:linear-gradient(135deg,#3b6fb0,#b5cbe6);width:100px;height:76px;margin-top:40px"></div>
  <h4>Simplicity Leads</h4><p>Lorem ipsum dolor sit amet, consectetur adipisici elit,</p><span class="more">READ MORE</span>
</div>

<section class="abs social-box">
  <div class="sb-head"><span class="sb-dot"></span><div><div class="sb-name">Bright Path Studio</div><span class="sb-like">Like</span></div></div>
  <div class="sb-count">1,277 people like <span style="color:#3b5177">Bright Path Studio</span>.</div>
  <div class="sb-faces" role="img" aria-label="Grid of follower profile pictures"></div>
  <div class="sb-foot"><i></i>Chatterly social plugin</div>
</section>

<footer class="abs footer"></footer>

<div class="abs f-col" style="left:139px;width:200px">
  <h3 class="f-head"><span class="hi">Contact</span> Info</h3>
  <div style="margin-top:26px">
    <div class="contact-row"><span class="ic"><svg width="10" height="13" viewBox="0 0 10 13"><path d="M5 0a5 5 0 0 0-5 5c0 3.5 5 8 5 8s5-4.5 5-8a5 5 0 0 0-5-5zm0 7a2 2 0 1 1 0-4 2 2 0 0 1 0 4z" fill="#ccc"/></svg></span><span>418 Harbour Lane,<br>Melbourne, Victoria 3000</span></div>
    <div class="contact-row"><span class="ic"><svg width="12" height="12" viewBox="0 0 12 12"><path d="M2.5 0 4.5 3 3.2 4.5a8 8 0 0 0 4.3 4.3L9 7.5l3 2L10.5 12C5 12 0 7 0 1.5z" fill="#ccc"/></svg></span><span>Phone: ( 555 ) 210 4471<br>Fax: ( 555 ) 210 4472</span></div>
    <div class="contact-row"><span class="ic"><svg width="12" height="9" viewBox="0 0 12 9"><rect width="12" height="9" fill="#ccc"/><path d="M0 0l6 5 6-5" fill="none" stroke="#3c3c3c"/></svg></span><span>admin@brightpathstudio.org<br>info@brightpathstudio.org</span></div>
  </div>
</div>

<div class="abs f-col" style="left:388px;width:200px">
  <h3 class="f-head"><span class="hi">Recent</span> Work</h3>
  <div class="works">
    <div role="img" aria-label="Thumbnail of a stressed woman" style="background:#a07a62"></div>
    <div role="img" aria-label="Thumbnail of a phrenology chart" style="background:#d4a43c"></div>
    <div role="img" aria-label="Thumbnail of a gear head illustration" style="background:#3c4654"></div>
    <div role="img" aria-label="Thumbnail of a counselling session" style="background:#c7c1b8"></div>
  </div>
</div>

<div class="abs f-col" style="left:642px;width:200px">
  <h3 class="f-head"><span class="hi">What</span> We Do</h3>
  <ul class="dolist">
    <li>Mauris lobortis leo eget cur</li><li>Nunc ultricies turpis eget di</li><li>Cras quis risus eu purus dignis</li>
    <li>Ut sit amet nulla sed antea</li><li>Fusce eleifend sapien non mau</li><li>Phasellus idrisus convallis</li>
  </ul>
</div>

<div class="abs f-col" style="left:883px;width:178px">
  <h3 class="f-head"><span class="hi">Upcoming</span> Events</h3>
  <div class="ev-thumb" role="img" aria-label="Photo of a thoughtful woman" style="background:linear-gradient(135deg,#e9e4dc,#9a6c4e)"></div>
  <div class="ev-title">Sem Porta Mollis Parturient</div>
  <div class="ev-meta">29/10/2014 , &nbsp;23 comments</div>
</div>

<div class="abs bottom">
  <div class="copy">Copyright © 2014 brightpathstudio.. All Rights Reserved. Terms &amp; Conditions</div>
  <span class="sq" style="left:939px"></span><span class="sq" style="left:971px"></span>
  <span class="sq" style="left:1003px"></span><span class="sq" style="left:1035px"></span>
</div>

</body>
</html>
```